About us:
Looking for eye catching cards for our 4D/HD Ultrasound Studio.

Description:
We are the premier 4D/HD Ultrasound studio in Pensacola/Pace as well as the greater panhandle area. We are a 4D/HD Ultrasound Studio in Pace, Florida, just a few minutes north of Pensacola. We offer 4D/HD imagining an early gender determination, 8 weeks by blood test and 14 weeks by ultrasound. We utilize the latest in 4D/HD technology to render beautiful images and memories that will last a lifetime.

At 4D Tiny Glimpse of Pace, we give a whole new meaning to ultrasounds. We utilize the most up-to-date 4D/HD ultrasound imaging, so we can provide clear, amazing images of your unborn baby to life. Will she have your nose or her Daddy's smile? Book your appointment today for an unforgettable experience. We also offer heartbeat animals.

Phone: 8505550147
www.4dtinyglimpse.example
address: 2716 -B HWY 38
Pace, FL 32590

Target Market(s)

Pregnant women

Requirements
Should not have
• Ultrasound training

```html
<!DOCTYPE html>
<html lang="en">
<head>
<meta charset="utf-8">
<title>4D Tiny Glimpse of Pace – Rack Cards</title>
<link rel="stylesheet" href="https://fonts.googleapis.com/css2?family=Poppins:ital,wght@0,300;0,400;0,600;0,700;1,700&family=Bebas+Neue&display=swap">
<style>
  :root {
    --stage: #5b5b5b;
    --white: #ffffff;
    --navy: #1e3454;
    --blue-deep: #2a4f7e;
    --blue-mid: #3c6395;
    --blue-bright: #3f5bb8;
    --blue-soft: #6f8fc0;
    --teal-ink: #2c5c66;
    --rose: #d0475a;
    --photo-dark: #3b3f46;
    --photo-light: #c9ccd2;
    --thumb: #b5524a;
  }
  * { margin: 0; padding: 0; box-sizing: border-box; }
  html, body {
    width: 1200px; height: 900px; overflow: hidden;
    background: var(--stage);
    font-family: "Poppins", sans-serif;
  }
  .canvas { position: relative; width: 1200px; height: 900px; }

  .card {
    position: absolute; top: 51px;
    width: 354px; height: 796px; overflow: hidden;
  }

  /* Front card */
  .card--front { left: 248px; background: var(--white); }
  .front-shapes { position: absolute; inset: 0; }
  .brand {
    position: absolute; display: flex; align-items: center; gap: 6px;
    font-family: "Poppins", sans-serif; font-weight: 400;
  }
  .brand--studio { left: 20px; top: 40px; font-size: 17px; color: var(--teal-ink); }
  .brand--studio .brand-dot {
    width: 12px; height: 12px; border-radius: 50%; background: var(--teal-ink);
  }
  .brand--partner {
    left: 208px; top: 34px; width: 130px; font-size: 15px; line-height: 1.15;
    color: var(--rose);
  }
  .front-title {
    position: absolute; left: 0; width: 100%; top: 178px;
    text-align: center; color: var(--white); font-weight: 300;
    line-height: 1;
  }
  .front-title span { display: block; }
  .front-title .t-4d { font-size: 76px; letter-spacing: 1px; }
  .front-title .t-ultra { font-size: 47px; margin-top: 6px; letter-spacing: -0.5px; }
  .front-title .t-sound { font-size: 80px; margin-top: 2px; }
  .front-photo {
    position: absolute; left: 0; right: 0; top: 480px; bottom: 0;
    background: linear-gradient(135deg, var(--photo-dark) 0%, #6f737a 45%, var(--photo-light) 100%);
    z-index: 0;
  }

  /* Back card */
  .card--back {
    left: 623px;
    background: linear-gradient(180deg, #3d5f8f 0%, #4f74a7 55%, #45669a 100%);
    color: var(--white);
  }
  .section-bar {
    position: absolute; left: 0; right: 0; height: 27px;
    background: var(--navy); text-align: center;
    font-weight: 600; font-size: 15px; line-height: 27px;
  }
  .section-bar--who { top: 25px; }
  .section-bar--offer { top: 181px; }
  .body-copy {
    position: absolute; left: 28px; right: 20px;
    font-weight: 300; font-size: 12.6px; line-height: 22px; letter-spacing: -0.2px;
  }
  .body-copy--who { top: 57px; }
  .body-copy--offer { top: 214px; }
  .thumb-strip {
    position: absolute; top: 364px; left: 20px; right: 20px;
    display: flex; justify-content: space-between; align-items: center;
  }
  .thumb { background: linear-gradient(135deg, #8e3a33, var(--thumb) 55%, #e0a28f); }
  .thumb--sm { width: 50px; height: 53px; }
  .thumb--lg { width: 62px; height: 62px; }
  .pitch {
    position: absolute; top: 452px; left: 18px; right: 18px; text-align: center;
    font-family: "Bebas Neue", sans-serif; font-size: 18.5px; line-height: 22px;
    letter-spacing: 0.1px;
  }
  .pitch-extra {
    position: absolute; top: 586px; left: 0; right: 0; text-align: center;
    font-weight: 700; font-style: italic; font-size: 12.5px; letter-spacing: 0.2px;
    text-transform: uppercase;
  }
  .cta-band {
    position: absolute; top: 628px; left: 0; right: 0; height: 60px;
    background: linear-gradient(90deg, #4f6fa8 0%, #7b98d0 50%, #4f6fa8 100%);
    text-align: center; font-family: "Bebas Neue", sans-serif;
    font-size: 25px; line-height: 25px; padding-top: 6px; color: #f3f6ff;
  }
  .contact {
    position: absolute; top: 702px; left: 0; right: 0; text-align: center;
    font-weight: 600; font-size: 13.3px; line-height: 20px; font-style: normal;
  }
</style>
</head>
<body>
<main class="canvas">

  <section class="card card--front">
    <svg class="front-shapes" width="354" height="796" viewBox="0 0 354 796" aria-hidden="true">
      <path d="M0 152 C70 168 150 150 210 110 C250 88 300 98 354 112 L354 480 L0 480 Z" fill="var(--blue-deep)"/>
      <path d="M0 440 C80 400 170 420 250 398 C300 384 330 386 354 400 L354 480 L0 480 Z" fill="var(--blue-bright)"/>
      <path d="M0 455 C90 418 180 440 260 420 C310 408 335 412 354 420 L354 470 L0 470 Z" fill="#34549a"/>
    </svg>
    <div class="front-photo" role="img" aria-label="Photo of a sonographer pointing at a 4D ultrasound screen while scanning an expectant mother"></div>
    <svg class="front-shapes" width="354" height="796" viewBox="0 0 354 796" aria-hidden="true">
      <path d="M0 430 C90 400 180 425 260 402 C310 390 335 392 354 398 L354 420 C300 428 240 440 170 460 C110 478 50 490 0 490 Z" fill="var(--blue-bright)"/>
      <path d="M0 420 C90 392 180 414 260 392 C310 380 335 384 354 390 L354 406 C300 416 240 430 170 450 C110 468 50 478 0 478 Z" fill="var(--blue-deep)"/>
    </svg>
    <div class="brand brand--studio"><span class="brand-dot"></span>4D Tiny Glimpse</div>
    <div class="brand brand--partner">Little Heartbeat Cub</div>
    <h1 class="front-title">
      <span class="t-4d">4D/HD</span>
      <span class="t-ultra">ULTRASOUND</span>
      <span class="t-sound">SOUND</span>
    </h1>
  </section>

  <section class="card card--back">
    <h2 class="section-bar section-bar--who">Who We Are</h2>
    <p class="body-copy body-copy--who">We are the premier 4D/HD Ultrasound studio in Pensacola/Pace as well as the greater panhandle area.<br>We are a 4D/HD Ultrasound Studio in Pace, Florida, just a few minutes north of Pensacola.</p>
    <h2 class="section-bar section-bar--offer">What We offer</h2>
    <p class="body-copy body-copy--offer">4D/HD imagining an early gender determination 8 weeks by blood test and 14 weeks by ultrasound.<br>We utilize the latest in 4D/HD technology to render beautiful images and memories that will last a lifetime.</p>
    <div class="thumb-strip">
      <div class="thumb thumb--sm" role="img" aria-label="4D ultrasound image of a baby in the womb"></div>
      <div class="thumb thumb--lg" role="img" aria-label="4D ultrasound image of a baby"></div>
      <div class="thumb thumb--lg" role="img" aria-label="4D ultrasound image of a baby"></div>
      <div class="thumb thumb--lg" role="img" aria-label="4D ultrasound image of a baby"></div>
      <div class="thumb thumb--sm" role="img" aria-label="4D ultrasound image of a baby"></div>
    </div>
    <p class="pitch">At 4D Tiny Glimpse of Pace, we give a whole new meaning to ultrasounds. We utilize the most up-to-date 4D/HD ultrasound imaging, so we can provide clear, amazing images of your unborn baby to life. Will she have your nose or her Daddy's smile?</p>
    <p class="pitch-extra">We also offer heartbeat animals.</p>
    <p class="cta-band">Book your appointment today for<br>an unforgettable experience.</p>
    <address class="contact">
      Phone: 8505550147<br>
      www.4dtinyglimpse.example<br>
      address: 2716 -B HWY 38<br>
      Pace, FL 32590
    </address>
  </section>

</main>
</body>
</html>
```